Tomas Verlund,M.D. Pediatric Office
Stationery, Envelopes and Biz Card
Bright & Fun-filled
Tomas Verlund,M.D.P.C.
Board Certified Pediatrician
3916 Pellingham Rd. Suite 204
Dearborn, MI 48391
tomas@verlundo.example
www.verlundo.example
Please use my logo on top and elements derived from my logo on other parts of stationery:
Suggestions: The boy and girl on the logo could be used in a playing or happy walking position at the bottom of the letterhead above the address and phone number area
and can be used at the addressee's area on the envelope in a wlcoming happy position. (Please feel free to be totally creative. I'm open to all suggestions and innovations).Different is good!!
Elements derived from logo
Be totally free and creative. You are the expert!

```html
<!DOCTYPE html>
<html lang="en">
<head>
<meta charset="utf-8">
<title>Tomas Verlund, M.D., P.C. — Stationery Set</title>
<link rel="stylesheet" href="https://fonts.googleapis.com/css2?family=Libre+Baskerville:wght@700&family=Arimo:wght@400;700&display=swap">
<style>
  :root {
    --stage: #8a8a8a;
    --paper: #ffffff;
    --green-deep: #6fae1e;
    --green: #8cc63f;
    --green-light: #d6ea9c;
    --blue: #2a6fb8;
    --orange: #f08a1c;
    --ink: #3b3b3b;
    --label: #ffffff;
    --art-a: #9fd9ef;
    --art-b: #f7c96a;
    --art-c: #e98bc4;
  }
  * { box-sizing: border-box; margin: 0; padding: 0; }
  html, body { width: 1200px; height: 648px; overflow: hidden; background: var(--stage); }
  body { font-family: "Arimo", Arial, sans-serif; color: var(--ink); position: relative; }

  .piece { position: absolute; background: var(--paper); overflow: hidden; box-shadow: 0 2px 5px rgba(0,0,0,.35); }
  .piece svg.swoosh { position: absolute; inset: 0; width: 100%; height: 100%; }
  .label { position: absolute; color: var(--label); font-size: 6px; font-weight: 700; letter-spacing: .3px; }

  .brand { position: absolute; display: flex; align-items: center; gap: 6px; }
  .brand-dot { border-radius: 50%; background: var(--green); flex: none; }
  .brand-name { font-family: "Libre Baskerville", Georgia, serif; font-weight: 700; color: var(--blue); white-space: nowrap; }
  .brand-tag { font-family: "Libre Baskerville", Georgia, serif; font-weight: 700; color: var(--orange); white-space: nowrap; }

  .art { position: absolute; border-radius: 10px;
         background: linear-gradient(135deg, var(--art-a), var(--art-b) 55%, var(--art-c)); }

  .contact { position: absolute; font-size: 7px; line-height: 1.45; color: var(--ink); }

  /* letterhead */
  .letterhead { left: 233px; top: 19px; width: 440px; height: 617px; }
  .letterhead .brand { left: 120px; top: 78px; }
  .letterhead .brand-dot { width: 42px; height: 42px; }
  .letterhead .brand-name { font-size: 17px; }
  .letterhead .brand-tag { font-size: 10px; margin-top: 2px; }
  .letterhead .art { right: 22px; bottom: 22px; width: 185px; height: 165px; }
  .letterhead .contact { left: 40px; bottom: 52px; font-size: 8px; }

  /* cards */
  .postcard-front { left: 22px; top: 211px; width: 190px; height: 150px; }
  .postcard-back  { left: 223px; top: 216px; width: 190px; height: 150px; }
  .card-front     { left: 22px; top: 420px; width: 190px; height: 137px; }
  .card-back      { left: 223px; top: 420px; width: 190px; height: 137px; }

  .small .brand { left: 20px; top: 34px; gap: 4px; }
  .small .brand-dot { width: 14px; height: 14px; }
  .small .brand-name { font-size: 7px; }
  .small .brand-tag { font-size: 4.5px; }
  .small .contact { font-size: 4.5px; left: 20px; top: 64px; }
  .small .contact.right { left: auto; right: 14px; top: auto; bottom: 12px; text-align: right; }

  .postcard-back .art { left: 16px; top: 40px; width: 48px; height: 40px; border-radius: 6px; }
  .postcard-back .stamp { position: absolute; right: 14px; top: 40px; width: 24px; height: 28px; border: 1px solid #bbb; }
  .postcard-back .lines { position: absolute; right: 14px; top: 80px; width: 82px; }
  .postcard-back .lines span { display: block; height: 1px; background: #aaa; margin-bottom: 9px; }
  .postcard-back .divider { position: absolute; left: 92px; top: 40px; width: 1px; height: 90px; background: #ccc; }

  .card-back .art { left: 70px; top: 38px; width: 48px; height: 38px; border-radius: 6px; }
  .card-back .tag-line { position: absolute; left: 0; right: 0; top: 82px; text-align: center; font-size: 4.5px; color: var(--ink); }

  /* envelopes */
  .env-square { left: 684px; top: 84px; width: 497px; height: 180px; }
  .env-square .brand { left: 200px; top: 66px; }
  .env-square .brand-dot { width: 36px; height: 36px; }
  .env-square .art { left: 244px; top: 52px; width: 64px; height: 56px; border-radius: 8px; }

  .env-long { left: 684px; top: 360px; width: 497px; height: 269px; }
  .env-long .art { right: 10px; bottom: 10px; width: 118px; height: 112px; }
  .env-long .contact { left: 12px; top: 168px; font-size: 6px; }
  .env-long .contact.bottom { left: 170px; top: 236px; }
</style>
</head>
<body>

  <!-- Letterhead -->
  <section class="piece letterhead">
    <svg class="swoosh" viewBox="0 0 440 617" preserveAspectRatio="none" aria-hidden="true">
      <defs>
        <linearGradient id="lh-g" x1="0" y1="0" x2="1" y2="1">
          <stop offset="0" stop-color="#d6ea9c"/><stop offset="1" stop-color="#6fae1e"/>
        </linearGradient>
      </defs>
      <path d="M150 0 H440 V70 Q300 10 150 0 Z" fill="url(#lh-g)"/>
      <path d="M0 560 Q220 520 440 470 V617 H0 Z" fill="url(#lh-g)"/>
    </svg>
    <div class="brand">
      <span class="brand-dot"></span>
      <div>
        <div class="brand-name">Tomas Verlund, M.D., P.C.</div>
        <div class="brand-tag">Board Certified Pediatrician</div>
      </div>
    </div>
    <div class="art" role="img" aria-label="Illustration of the boy and girl from the logo playing"></div>
    <div class="contact">
      3916 Pellingham Rd. Suite 204<br>
      Dearborn, MI 48391<br>
      P: 313-555-0142<br>
      F: 313-555-0187<br>
      tomas@verlundo.example<br>
      www.verlundo.example
    </div>
  </section>

  <!-- Post card front -->
  <span class="label" style="left:60px; top:203px;">POST CARD FRONT</span>
  <section class="piece small postcard-front">
    <svg class="swoosh" viewBox="0 0 190 150" preserveAspectRatio="none" aria-hidden="true">
      <path d="M0 0 H190 V22 Q100 8 0 22 Z" fill="#8cc63f"/>
      <path d="M0 150 H190 V118 Q90 140 0 128 Z" fill="#8cc63f"/>
    </svg>
    <div class="brand"><span class="brand-dot"></span><div><div class="brand-name">Tomas Verlund, M.D., P.C.</div><div class="brand-tag">Board Certified Pediatrician</div></div></div>
    <div class="contact">3916 Pellingham Rd. Suite 204<br>Dearborn, MI 48391<br>P: 313-555-0142<br>F: 313-555-0187</div>
    <div class="contact right">tomas@verlundo.example<br>www.verlundo.example</div>
  </section>

  <!-- Post card back -->
  <span class="label" style="left:290px; top:208px;">POST CARD BACK</span>
  <section class="piece postcard-back">
    <svg class="swoosh" viewBox="0 0 190 150" preserveAspectRatio="none" aria-hidden="true">
      <path d="M0 0 H190 V26 Q90 6 0 22 Z" fill="#8cc63f"/>
    </svg>
    <div class="art" role="img" aria-label="Small illustration of the logo children"></div>
    <span class="divider"></span>
    <span class="stamp"></span>
    <div class="lines"><span></span><span></span><span></span><span></span></div>
  </section>

  <!-- Business card front -->
  <span class="label" style="left:64px; top:412px;">Biz CARD FRONT</span>
  <section class="piece small card-front">
    <svg class="swoosh" viewBox="0 0 190 137" preserveAspectRatio="none" aria-hidden="true">
      <path d="M0 0 H190 V20 Q100 6 0 20 Z" fill="#8cc63f"/>
      <path d="M0 137 H190 V110 Q90 130 0 118 Z" fill="#8cc63f"/>
    </svg>
    <div class="brand"><span class="brand-dot"></span><div><div class="brand-name">Tomas Verlund, M.D., P.C.</div><div class="brand-tag">Board Certified Pediatrician</div></div></div>
    <div class="contact">3916 Pellingham Rd. Suite 204<br>Dearborn, MI 48391<br>P: 313-555-0142<br>F: 313-555-0187</div>
    <div class="contact right">tomas@verlundo.example<br>www.verlundo.example</div>
  </section>

  <!-- Business card back -->
  <span class="label" style="left:268px; top:412px;">Biz CARD BACK</span>
  <section class="piece card-back">
    <svg class="swoosh" viewBox="0 0 190 137" preserveAspectRatio="none" aria-hidden="true">
      <defs>
        <linearGradient id="cb-g" x1="0" y1="0" x2="1" y2="1">
          <stop offset="0" stop-color="#d6ea9c"/><stop offset="1" stop-color="#6fae1e"/>
        </linearGradient>
      </defs>
      <rect width="190" height="137" fill="url(#cb-g)"/>
    </svg>
    <div class="art" role="img" aria-label="Logo children illustration"></div>
    <div class="tag-line">Board Certified Pediatrician</div>
  </section>

  <!-- Square envelope -->
  <section class="piece env-square">
    <svg class="swoosh" viewBox="0 0 497 180" preserveAspectRatio="none" aria-hidden="true">
      <defs>
        <linearGradient id="es-g" x1="0" y1="0" x2="1" y2="0">
          <stop offset="0" stop-color="#6fae1e"/><stop offset=".5" stop-color="#d6ea9c"/><stop offset="1" stop-color="#6fae1e"/>
        </linearGradient>
      </defs>
      <path d="M0 0 H497 V40 L248 110 L0 40 Z" fill="url(#es-g)"/>
      <path d="M0 150 Q248 130 497 150 V180 H0 Z" fill="#8cc63f"/>
    </svg>
    <div class="art" role="img" aria-label="Logo children illustration on the flap"></div>
  </section>

  <!-- Long envelope -->
  <section class="piece env-long">
    <svg class="swoosh" viewBox="0 0 497 269" preserveAspectRatio="none" aria-hidden="true">
      <defs>
        <linearGradient id="el-g" x1="0" y1="0" x2="1" y2="1">
          <stop offset="0" stop-color="#6fae1e"/><stop offset="1" stop-color="#d6ea9c"/>
        </linearGradient>
      </defs>
      <path d="M0 0 H200 Q80 90 0 150 Z" fill="url(#el-g)"/>
      <path d="M0 225 Q250 210 497 160 V269 H0 Z" fill="url(#el-g)"/>
    </svg>
    <div class="contact">3916 Pellingham Rd. Suite 204 Dearborn, MI 48391<br>P: 313-555-0142 &nbsp; F: 313-555-0187</div>
    <div class="contact bottom">tomas@verlundo.example &nbsp;&nbsp; www.verlundo.example</div>
    <div class="art" role="img" aria-label="Boy and girl from the logo welcoming near the addressee area"></div>
  </section>

</body>
</html>
```